Attorney Website Design

I need a top quality attorney website layout designed. Here are some examples of what I feel are great websites:
http://www.quellmarstonseparationlaw.com/
http://www.vandriclegalgroup.com/
http://www.pobelaw.com/
http://www.harrowvaleaccusedcounselhq.com/
http://www.tzlegal.com/
http://www.brookhollowtrialjusticeoffice.com/
http://www.orvynchargedcounsel.com/
http://www.tzlegal.com/
What we like about these sites:
• The different layers
• Subtle designs, textures, curves
• 3 dimensional
• Floating effects
• Prominent phone number
• Location of Areas of Practice
• Request A Consultation Prominent
• Right side bar with practice areas
• Badges
• Clear Calls to Action
• Dynamic/Staying Top navigation when you scroll
The project will be for a home page and then also an interior page (should be similar to home page).
Updates
I want to make it understood I am looking for a design which is not a typical "template" site which I can find anywhere for $50. This budget and project is for a "Custom" website design. Please submit designs similar in quality to the samples links I have posted. Creativity is a MUST! The best way to explain this is, I want a design that I can feel it unique and original, not something that looks like 95% of all websites out there.
Neil
I just wanted everyone to know that so far I am not to pleased with any of the designs. I am not looking for cut/pasting of other peoples websites but ORIGINAL and CREATIVE work.
Reason: Weekend + Holiday extension.
Reason: Need more designs
Industry/Entity Type
Attorney

```html
<!DOCTYPE html>
<html lang="en">
<head>
<meta charset="utf-8">
<title>Brookhollow Attorneys</title>
<link href="https://fonts.googleapis.com/css2?family=Open+Sans:wght@400;600;700&family=Tinos:wght@400;700&display=swap" rel="stylesheet">
<style>
:root{
  --red:#b30c0c;
  --red-dark:#8e0707;
  --ink:#2f2f2f;
  --muted:#8a8a8a;
  --light:#f4f4f4;
  --footer:#2b2b2b;
  --footer-bottom:#1e1e1e;
  --footer-text:#c9c9c9;
}
*{margin:0;padding:0;box-sizing:border-box}
html,body{width:802px;height:1200px;overflow:hidden}
body{position:relative;background:#fff;font-family:"Open Sans",Arial,sans-serif;color:var(--ink)}
.abs{position:absolute}

.site-header{left:0;top:0;width:802px;height:74px;background:#fff}
.header-panel{right:0;top:0;width:340px;height:74px;background:linear-gradient(90deg,#f2f2f2,#e4e4e4)}
.brand{left:74px;top:24px;font-family:"Open Sans",Arial,sans-serif;font-size:20px;font-weight:600;color:var(--red);line-height:1;white-space:nowrap}
.counsel{left:576px;top:15px;font-size:7.5px;font-weight:700;line-height:1.1;color:#555}
.counsel span{display:block;color:#3f6fa8;font-style:italic}
.counsel-rule{left:533px;top:36px;width:196px;height:1px;background:#b8b8b8}
.phone{left:576px;top:40px;font-size:20px;color:var(--red);letter-spacing:.3px}

.main-nav{left:0;top:74px;width:802px;height:33px;background:var(--red);border-bottom:1px solid var(--red-dark)}
.nav-list{left:81px;top:7px;display:flex;list-style:none}
.nav-list li{font-size:11px;color:#fff;padding:3px 9px;margin-right:1px}
.nav-list li.active{background:#3b0a0a;border-radius:2px}
.search{left:567px;top:8px;width:162px;height:19px;background:#fff;border-radius:2px;font-size:9px;color:#666;padding:4px 6px}
.search-btn{left:704px;top:8px;width:25px;height:19px;background:#3b0a0a;border-radius:0 2px 2px 0}

.hero-photo{left:0;top:107px;width:802px;height:333px;background:linear-gradient(110deg,#6a5220 0%,#a98a45 35%,#c7b27a 55%,#5a4a22 80%,#2f2713 100%)}
.welcome{left:74px;top:187px;width:292px;height:168px;background:rgba(242,242,242,.94);padding:15px 13px}
.welcome h1{font-family:"Tinos",serif;font-weight:400;font-size:18px;line-height:1.25;color:#333;white-space:nowrap}
.welcome h1 strong{display:block;color:var(--red);font-weight:700;font-size:17.5px}
.welcome p{font-size:8.4px;line-height:1.3;color:#555;margin-top:10px}
.btn{display:inline-block;background:var(--red);color:#fff;font-weight:600;border-radius:2px;box-shadow:0 1px 2px rgba(0,0,0,.3)}
.welcome .btn{margin-top:13px;font-size:10.5px;padding:6px 10px}

.services{left:0;top:440px;width:802px;height:281px;background:var(--light)}
.card{top:38px;width:142px}
.card-img{width:142px;height:88px;border:2px solid #fff;box-shadow:0 2px 4px rgba(0,0,0,.2)}
.card h2{font-size:10.3px;font-weight:400;margin-top:13px;color:#222;white-space:nowrap}
.card p{font-size:8.2px;line-height:12px;color:var(--muted);margin-top:7px;height:60px;overflow:hidden}
.card hr{border:0;border-top:1px solid #d6d6d6;margin-top:6px}
.card a{display:block;font-size:8.6px;color:var(--red);text-decoration:underline;margin-top:5px}

.videos{left:0;top:721px;width:802px;height:261px}
.videos h2{left:74px;top:36px;font-size:20px;font-weight:600;letter-spacing:.3px}
.videos .copy{left:74px;top:68px;width:322px;font-size:8.3px;line-height:1.6;color:var(--muted)}
.videos .copy p+p{margin-top:13px}
.videos .btn{left:74px;top:199px;font-size:9.6px;padding:6px 16px}
.video-frame{left:415px;top:40px;width:314px;height:184px;background:linear-gradient(120deg,#2a1a14,#6d4335 55%,#3a231b)}
.video-bar{left:415px;top:202px;width:314px;height:22px;background:#1a1a1a}

.site-footer{left:0;top:982px;width:802px;height:186px;background:var(--footer);color:var(--footer-text)}
.f-col{top:28px}
.f-col h3{font-size:8px;font-weight:700;color:#fff;display:flex;align-items:center;gap:6px}
.f-col h3::after{content:"";flex:1;display:block;height:3px;border-top:1px dotted #777;border-bottom:1px dotted #777}
.f-col ul{list-style:none;margin-top:11px}
.f-col li{font-size:8.4px;line-height:14.7px}
.f-col li::before{content:"›";margin-right:7px;color:#999}
.f-col li.current{color:#e52020}
.info-row{display:flex;gap:10px;font-size:8.4px;line-height:1.4;margin-top:9px}
.info-ico{width:11px;height:11px;border-radius:2px;background:#8d8d8d;flex:none;margin-top:1px}
.social{left:76px;top:136px;width:115px;height:24px;background:#333;border-radius:3px;display:flex;gap:5px;padding:3px 4px}
.social i{width:18px;height:18px;border-radius:50%;background:#8d8d8d}
.map{left:591px;top:49px;width:130px;height:97px;background:linear-gradient(135deg,#e8e6de,#d9d6ca)}
.bottom-bar{left:0;top:1168px;width:802px;height:32px;background:var(--footer-bottom);color:var(--footer-text);font-size:8.4px}
.bottom-bar .copy{left:75px;top:10px}
.bottom-bar .legal{right:74px;top:10px}
</style>
</head>
<body>
<header class="site-header abs">
  <div class="header-panel abs"></div>
  <div class="brand abs">Brookhollow Attorneys</div>
  <svg class="abs" style="left:534px;top:14px" width="32" height="22" viewBox="0 0 32 22"><path d="M3 20V8h6l3-5h10v5h6v12z" fill="none" stroke="#999" stroke-width="2"/></svg>
  <div class="counsel abs">Don't hesitate for legal counsel<span>Call for a free case evaluation</span></div>
  <div class="counsel-rule abs"></div>
  <div class="phone abs">123 456 7890</div>
</header>

<nav class="main-nav abs">
  <ul class="nav-list abs">
    <li class="active">Home</li><li>Know Your Rights</li><li>Check The News</li><li>Read Articles</li><li>Contact US</li>
  </ul>
  <div class="search abs">Search</div>
  <div class="search-btn abs"><svg width="25" height="19" viewBox="0 0 25 19"><circle cx="11.5" cy="8.5" r="4" fill="none" stroke="#fff" stroke-width="1.8"/><path d="M14.5 11.5l3 3" stroke="#fff" stroke-width="1.8"/></svg></div>
</nav>

<section>
  <div class="hero-photo abs" role="img" aria-label="Sepia photo of an empty courtroom with brass scales of justice on a bench"></div>
  <div class="welcome abs">
    <h1>WELCOME TO<strong>BROOKHOLLOW ATTORNEYS</strong></h1>
    <p>Lorem ipsum dolor sit amet, consectetur adipisicing elit, sed do eiusmod tempor incididunt ut labore et dolore magna aliqua. Ut enim ad minim veniam, quis nostrud exercitation ullamco laboris nisi ut aliquip ex ea commodo consequat.</p>
    <span class="btn">CONSULTATION</span>
  </div>
</section>

<section class="services abs">
  <article class="card abs" style="left:74px">
    <div class="card-img" role="img" aria-label="Photo of two lawyers in an office" style="background:linear-gradient(90deg,#7d6a5c,#c9c4bc 50%,#6f7680)"></div>
    <h2>FLORIDA DIVORCE LAWYER</h2>
    <p>Lorem ipsum dolor sit amet consectetur adipisicing elit, sed do eiusmod tempor incididunt labore et dolore magna aliqua. Ut enim ad minim veniam, quis</p>
    <hr><a>Read More</a>
  </article>
  <article class="card abs" style="left:243px">
    <div class="card-img" role="img" aria-label="Photo of a divorce decree document with a pen" style="background:linear-gradient(135deg,#e6e2d2,#cfc8b0 60%,#9a8e6c)"></div>
    <h2>DIVORCE LAW ATTORNEYS</h2>
    <p>Lorem ipsum dolor sit amet consectetur adipisicing elit, sed do eiusmod tempor incididunt labore et dolore magna aliqua. Ut enim ad minim veniam, quis</p>
    <hr><a>Read More</a>
  </article>
  <article class="card abs" style="left:413px">
    <div class="card-img" role="img" aria-label="Photo of an open book and a gavel" style="background:linear-gradient(135deg,#6b4526,#b99468 50%,#3c2616)"></div>
    <h2>MIAMI ATTORNEYS</h2>
    <p>Lorem ipsum dolor sit amet consectetur adipisicing elit, sed do eiusmod tempor incididunt labore et dolore magna aliqua. Ut enim ad minim veniam, quis</p>
    <hr><a>Read More</a>
  </article>
  <article class="card abs" style="left:584px">
    <div class="card-img" role="img" aria-label="Photo of a justice statue with scales and gavel" style="background:linear-gradient(135deg,#2e1812,#6b3d30 55%,#3a2019)"></div>
    <h2>ATTORNEYS IN TAMPA</h2>
    <p>Lorem ipsum dolor sit amet consectetur adipisicing elit, sed do eiusmod tempor incididunt labore et dolore magna aliqua. Ut enim ad minim veniam, quis</p>
    <hr><a>Read More</a>
  </article>
</section>

<section class="videos abs">
  <h2 class="abs">VIDEOS</h2>
  <div class="copy abs">
    <p>Lorem ipsum dolor sit amet, consectetur adipisicing elit, sed do eiusmod tempor incididunt ut labore&nbsp; dolore magna aliqua ut enim ad minim veniam quis nostrud exercitation ullamco laboris nisi ut aliquip ex ea commodo consequat duis aute irure dolor in reprehenderit in voluptate.</p>
    <p>&nbsp;velit esse cillum dolore eu fugiat nulla pariatur. Excepteur sint occaecat cupidatat non proident, sunt in culpa qui officia deserunt mollit anim id est laborum lorem ipsum dolor sit amet, consectetur adipisicing elit, sed do eiusmod tempor.</p>
  </div>
  <span class="btn abs">READ MORE</span>
  <div class="video-frame abs" role="img" aria-label="Video still of a justice statue holding scales beside a gavel"></div>
  <svg class="abs" style="left:549px;top:100px" width="44" height="44" viewBox="0 0 44 44"><circle cx="22" cy="22" r="22" fill="#1a1a1a" opacity=".85"/><path d="M17 13l14 9-14 9z" fill="#fff"/></svg>
  <div class="video-bar abs">
    <svg width="314" height="22" viewBox="0 0 314 22">
      <rect x="0" y="0" width="314" height="4" fill="#555"/><rect x="0" y="0" width="34" height="4" fill="#c31a1a"/><circle cx="34" cy="2" r="4" fill="#ddd"/>
      <rect x="16" y="10" width="2.5" height="8" fill="#ddd"/><rect x="21" y="10" width="2.5" height="8" fill="#ddd"/>
      <path d="M43 12h3l4-3v10l-4-3h-3z" fill="#ddd"/><rect x="63" y="14" width="38" height="2" fill="#777"/><rect x="63" y="11" width="3" height="8" fill="#ddd"/>
      <text x="225" y="17" font-size="7.5" fill="#ddd" font-family="Open Sans,sans-serif">0:14 / 3:25</text>
      <rect x="272" y="10" width="8" height="7" fill="#c31a1a"/><path d="M287 18v-6h6M302 10h4v4M306 18h-4M298 14v4h4" stroke="#ddd" fill="none" stroke-width="1.3"/>
    </svg>
  </div>
</section>

<footer class="site-footer abs">
  <div class="f-col abs" style="left:80px;width:145px">
    <h3>COMPANY INFO</h3>
    <div class="info-row" style="margin-top:12px"><span class="info-ico"></span><span>Lorem ipsum dolor sit amet consectetur adipisicing elit,</span></div>
    <div class="info-row"><span class="info-ico"></span><span>123-456-7890</span></div>
    <div class="info-row"><span class="info-ico"></span><span>companyinfo@brookmail.com</span></div>
  </div>
  <div class="social abs"><i></i><i></i><i></i><i></i><i></i></div>
  <div class="f-col abs" style="left:258px;width:145px">
    <h3>OUR SERVICES</h3>
    <ul><li>Criminal Defense Attorney</li><li>Florida Divorce Lawyer</li><li>Divorce Law Attorneys</li><li>Miami Attorneys</li><li>Attorneys Orlando FL</li><li>Attorneys in Tampa</li><li>Divorce Attorneys Tampa FL</li><li>Florida Criminal Attorneys</li></ul>
  </div>
  <div class="f-col abs" style="left:438px;width:118px">
    <h3>SITE MAP</h3>
    <ul><li class="current">Home</li><li>Know Your Rights</li><li>Check The News</li><li>Read Articles</li><li>Contact US</li></ul>
  </div>
  <div class="f-col abs" style="left:590px;width:135px"><h3>FIND US</h3></div>
  <div class="map abs" role="img" aria-label="Street map showing the office location"></div>
</footer>

<div class="bottom-bar abs">
  <span class="copy abs">Copy righte 2014 © Brookhollow Attorneys. All rights reserved</span>
  <span class="legal abs">Terms &amp; Condition &nbsp;| &nbsp;Privacy Policy</span>
</div>
</body>
</html>
```